Powepoint Templates From Logo

We need 3 Powerpoint templates for use in a variety of presentations we develop and customize. Primary uses of the powerpoint presentations are for printed "pitch books" describing our firm's capabilities and approach (a lot of words with some design elements that we have developed), printed presentations of the results of financial evaluations of our clients (lots of charts and graphs) and as the talking points for speeches.

The design needs to be professional and "solid" to establish that we are capable of selling your multi-million dollar business, but also be a little different to show that we are not just boring MBA's.

Our current website and other materials have been developed internally and leave a great deal to be desired. I have initiated this project to demonstrate how much our look can be improved and, if successful, I hope to do much bigger projects in the future.
Updates

This is my first project and I thaank you all for your participation. Since I am new to this, I don;t know if I am providing the help and feedback as I should. Please feel free to let me know how I can be a better customer.

Target Market(s)

professionals (lawyers, accountaants), business owners, business groups, technology people

Industry/Entity Type

Financial

Requirements
Must have
• our logo
a place where logo of client can be inserted if appropriate
templates for the following pages
title page
standard bullet narrative page
page for charts and graphs to mostly fill the page
Should not have a lot of dark solid color that has to be printed.

Nice to have
• something to perk up the color a little

```html
<!DOCTYPE html>
<html lang="en">
<head>
<meta charset="utf-8">
<title>Chart Slide</title>
<link rel="stylesheet" href="https://fonts.googleapis.com/css2?family=Source+Sans+3:wght@400;600&display=swap">
<style>
  :root {
    --navy: #1c2f5e;
    --ink-grey: #666a70;
    --paper: #ffffff;
    --stage: #d7d9dc;
    --slide-light: #f7f7f7;
    --slide-edge: #e1e2e4;
    --grid: #222222;
    --client-green: #3a9a3e;
    --bar-orange: #f08a3c;
    --bar-blue: #3aa3e0;
  }
  * { margin: 0; padding: 0; box-sizing: border-box; }
  html, body { width: 1200px; height: 900px; overflow: hidden; background: var(--stage); }
  body { font-family: "Source Sans 3", Arial, sans-serif; position: relative; }

  .slide {
    position: absolute; left: 17px; top: 14px; width: 1170px; height: 862px;
    background: radial-gradient(ellipse at 50% 40%, var(--slide-light) 0%, var(--slide-light) 30%, var(--slide-edge) 100%);
    box-shadow: 2px 3px 6px rgba(0,0,0,0.35);
    overflow: hidden;
  }
  .slide-header {
    position: absolute; left: 0; top: 0; width: 100%; height: 116px;
    background: var(--paper);
    border-bottom: 8px solid var(--navy);
  }
  .firm-name {
    position: absolute; left: 30px; top: 46px;
    display: flex; align-items: center; gap: 10px;
    color: var(--navy); font-weight: 600; font-size: 26px; letter-spacing: 0.5px;
  }
  .firm-name .mark { width: 22px; height: 22px; border: 3px solid var(--navy); border-radius: 4px; }
  .client-name {
    position: absolute; right: 32px; top: 58px;
    color: var(--client-green); font-size: 27px; font-weight: 400;
  }

  .chart-heading {
    position: absolute; top: 240px; width: 436px; text-align: center;
    color: var(--navy); font-size: 40px; font-weight: 400;
  }
  .chart-heading.left { left: 99px; }
  .chart-heading.right { left: 633px; }

  .chart-card {
    position: absolute; top: 324px; width: 436px; height: 436px;
    background: var(--paper); border: 2px solid var(--navy); border-radius: 16px;
  }
  .chart-card.left { left: 99px; }
  .chart-card.right { left: 633px; }
  .card-title {
    position: absolute; left: 42px; top: 14px;
    color: var(--ink-grey); font-size: 29px; font-weight: 400;
  }
  .line-chart {
    position: absolute; left: 14px; top: 94px; width: 398px; height: 246px;
    border: 1px solid #555; background: var(--paper);
  }
  .line-chart text { font-family: Arial, sans-serif; font-size: 9px; fill: #222; }
  .bar-chart-art {
    position: absolute; left: 84px; top: 108px; width: 298px; height: 293px;
    border-radius: 6px;
    background: linear-gradient(135deg, var(--bar-orange) 0%, #f9c38f 45%, #8fd0f3 55%, var(--bar-blue) 100%);
    opacity: 0.85;
  }

  .footnote {
    position: absolute; left: 198px; top: 784px;
    color: var(--ink-grey); font-size: 18px;
  }
  .page-corner {
    position: absolute; left: 0; bottom: 0; width: 76px; height: 76px;
    background: var(--navy); clip-path: polygon(0 0, 100% 100%, 0 100%);
  }
  .page-number {
    position: absolute; left: 9px; bottom: 6px;
    color: var(--paper); font-size: 27px;
  }
  .slide-footer {
    position: absolute; left: 0; bottom: 0; width: 100%; height: 7px; background: var(--navy);
  }
</style>
</head>
<body>
  <div class="slide">
    <header class="slide-header">
      <div class="firm-name"><span class="mark"></span>HALBERD PARTNERS</div>
      <div class="client-name">Client Name</div>
    </header>

    <h2 class="chart-heading left">Chart#1</h2>
    <h2 class="chart-heading right">Chart#1</h2>

    <section class="chart-card left">
      <h3 class="card-title">Expansion Rate 2014</h3>
      <svg class="line-chart" viewBox="0 0 398 246" aria-label="Expansion rate line chart">
        <g stroke="var(--grid)" stroke-width="0.8" fill="none">
          <rect x="58" y="16" width="327" height="174"/>
          <path d="M90.7 16V190M123.4 16V190M156.1 16V190M188.8 16V190M221.5 16V190M254.2 16V190M286.9 16V190M319.6 16V190M352.3 16V190"/>
          <path d="M58 45H385M58 74H385M58 103H385M58 132H385M58 161H385"/>
        </g>
        <path d="M58.3 190L59 162L61.3 132L64.5 114.6L74.4 91.4L90.7 74L123.4 56.6L156 46.2L221.5 33.4L287 24.7L385 16"
              fill="none" stroke="#000" stroke-width="2.2" stroke-linejoin="round"/>
        <g text-anchor="end">
          <text x="50" y="19">2</text><text x="50" y="48">1.5</text><text x="50" y="77">1</text>
          <text x="50" y="106">0.5</text><text x="50" y="135">0</text><text x="50" y="164">-0.5</text>
          <text x="50" y="193">-1</text>
        </g>
        <text x="24" y="103" transform="rotate(-90 24 103)" text-anchor="middle">log10 (x)</text>
        <g text-anchor="middle">
          <text x="58" y="206">0</text><text x="90.7" y="206">10</text><text x="123.4" y="206">20</text>
          <text x="156.1" y="206">30</text><text x="188.8" y="206">40</text><text x="221.5" y="206">50</text>
          <text x="254.2" y="206">60</text><text x="286.9" y="206">70</text><text x="319.6" y="206">80</text>
          <text x="352.3" y="206">90</text><text x="385" y="206">100</text>
        </g>
      </svg>
    </section>

    <section class="chart-card right">
      <h3 class="card-title">Growth Rate 2015</h3>
      <div class="bar-chart-art" role="img" aria-label="3D bar chart of orange and blue columns for values 120 to 150"></div>
    </section>

    <p class="footnote">* Of expected franchice exp.</p>

    <div class="page-corner"></div>
    <div class="page-number">3.</div>
    <div class="slide-footer"></div>
  </div>
</body>
</html>
```